A 'new law' boutique Australian law firm that provides specialist employment law and people managem

We value helping clients create results with respect workplaces. What differentiates us is we provide actionable training in understanding and dealing with people and ensure legal compliance fits with this approach. We would like a fresh approach to our training overview documents that we currently use in our current law firm (6 attached). Please use pictures, symbols etc consistent with our non-traditional law approach that captures the approach of each training session.. Attached is the logo and draft letterhead for Brook Legal which will launch soon.

Target Market(s)

HR Managers and in-house lawyers (non employment specialists) in mid-large Australian companies that are progressive with a relationship based approach to managing employee behaviours and disputes.

Industry/Entity Type

Human Resource

Font styles to use
Sans Serif

Colors
3176b5
33a6d7

Requirements
Must have
• 1 or 2 page PDF for each of the 6 documents that the wording supplied goes into your design which will be pretty similar as we want consistency with our documents

```html
<!DOCTYPE html>
<html lang="en">
<head>
<meta charset="utf-8">
<title>Contact Officer Training – Brook Legal</title>
<link rel="stylesheet" href="https://fonts.googleapis.com/css2?family=Oswald:wght@500;600&family=Montserrat:wght@500;600;700&family=Lato:wght@400;700&display=swap">
<style>
:root{
  --backdrop:#2a2a2a;
  --paper:#ffffff;
  --mist:#e2e3e5;
  --navy:#1d6cb2;
  --bright:#1f8ae6;
  --sky:#4ba9f2;
  --slate:#424242;
  --ink:#2b2b2b;
}
*{margin:0;padding:0;box-sizing:border-box}
html,body{width:1200px;height:1200px;overflow:hidden;background:var(--backdrop)}
body{position:relative;font-family:"Lato",sans-serif;color:var(--ink)}
.page{position:absolute;width:461px;height:646px;background:var(--paper);overflow:hidden;box-shadow:0 10px 30px rgba(0,0,0,.55)}
.page--front{left:102px;top:318px}
.page--back{left:633px;top:312px}
.abs{position:absolute}

/* brand name */
.brand{display:flex;align-items:center;gap:7px;font-family:"Montserrat",sans-serif;font-weight:600;font-size:20px;white-space:nowrap}
.brand__dot{width:12px;height:12px;border-radius:50%;display:inline-block;flex:none}

/* front header */
.front-header{left:0;top:0;width:461px;height:90px;background:var(--mist)}
.front-brand{left:40px;top:36px;color:var(--navy)}
.front-brand .brand__dot{background:var(--navy)}
.title-small{left:250px;top:9px;font-family:"Oswald",sans-serif;font-weight:500;font-size:30px;line-height:1;color:#2f2f2f;letter-spacing:-.3px}
.title-big{left:250px;top:41px;font-family:"Oswald",sans-serif;font-weight:600;font-size:50px;line-height:1;color:var(--navy);letter-spacing:-.5px}

.photo{left:0;top:90px;width:236px;height:294px;background:linear-gradient(160deg,#dfe6ee 0%,#b9c6d3 45%,#7c8897 100%)}
.need{left:251px;top:91px;width:210px;height:292px;background:var(--navy);color:#fff;padding:24px 12px 0 13px}
.need h2{font-family:"Montserrat",sans-serif;font-weight:500;font-size:12px;margin-bottom:9px}
.need p{font-size:7.3px;line-height:1.42;text-align:justify;margin-bottom:8px;margin-left:2px}

.overview-pill{left:46px;top:404px;width:368px;height:24px;background:var(--bright);border-radius:4px;color:#fff;font-family:"Montserrat",sans-serif;font-weight:600;font-size:13.5px;letter-spacing:.5px;text-align:center;line-height:24px;box-shadow:0 2px 3px rgba(0,0,0,.25);z-index:2}
.overview{left:0;top:416px;width:461px;height:182px;background:var(--slate)}
.overview-divider{left:239px;top:442px;width:1px;height:150px;background:#888}
.topic{color:#e8e8e8;font-size:7.1px;line-height:1.3}
.topic h3{font-family:"Montserrat",sans-serif;font-weight:600;font-size:8.8px;color:var(--sky);display:flex;align-items:center;gap:5px;margin-bottom:2px}
.topic h3 svg{flex:none}
.topic p{text-align:justify}

.footer-line{font-family:"Montserrat",sans-serif;font-size:7.6px;color:#222;display:flex;align-items:center;gap:10px;margin-bottom:3px}
.social{font-family:"Montserrat",sans-serif;font-weight:600;font-size:6px;color:#222;display:flex;align-items:center;gap:6px;margin-bottom:4px}
.social i{width:5px;height:5px;border-radius:50%;background:#555;display:inline-block}
.front-bar{left:0;top:640px;width:461px;height:6px;background:var(--bright)}

/* back */
.back-dark{left:0;top:21px;width:461px;height:201px;background:var(--slate)}
.back-divider{left:242px;top:35px;width:1px;height:163px;background:#8a8a8a}
.outcomes-bar{left:47px;top:242px;width:366px;height:18px;background:var(--sky);border-radius:3px;font-family:"Montserrat",sans-serif;font-weight:600;font-size:13px;color:#2d2d2d;text-align:center;line-height:19px;letter-spacing:.3px;box-shadow:0 3px 3px -2px rgba(0,0,0,.3)}
.outcomes-intro{left:60px;top:281px;width:341px;text-align:center;font-size:10px;line-height:1.3;color:#222}
.outcomes{left:36px;top:328px;width:400px;list-style:none}
.outcomes li{display:flex;align-items:flex-start;gap:9px;font-family:"Montserrat",sans-serif;font-size:8.8px;line-height:1.2;color:#222;margin-bottom:8.4px}
.outcomes li svg{flex:none;margin-top:-1px}
.contact-band{left:0;top:498px;width:461px;height:83px;background:var(--bright);color:#fff}
.contact-list{left:40px;top:13px;font-family:"Montserrat",sans-serif;font-size:8.3px;line-height:15px}
.contact-list div{display:flex;align-items:center;gap:6px}
.back-brand{left:305px;top:31px;color:#fff}
.back-brand .brand__dot{background:#fff}
.back-bottom{left:0;top:640px;width:461px;height:6px;background:var(--slate)}
</style>
</head>
<body>

<section class="page page--front">
  <div class="abs front-header"></div>
  <div class="abs brand front-brand"><span class="brand__dot"></span>Brook Legal</div>
  <div class="abs title-small">CONTACT OFFICER</div>
  <div class="abs title-big">TRAINING</div>

  <div class="abs photo" role="img" aria-label="Photo of colleagues reviewing charts together at a meeting table in a bright office"></div>

  <div class="abs need">
    <h2>TRAINING NEED</h2>
    <p><strong>Unlawful or inappropriate</strong> behavior in the workplace that is left unaddressed can impact on productivity and employee retention. Claims can be costly in terms of time and money as well as the impact on mental health from being involved in uncomfortable adversarial processes.</p>
    <p>Clear policies and procedures explaining the organisation's workplace behavior expectations and how grievances will be managed are a minimum compliance requirement.</p>
    <p>The challenge is ensuring that employees understand the directions contained in those policies, what is unlawful and inappropriate behaviour and the options available to address those behaviours if they experience them or engage in them.</p>
    <p>Well trained Contact Officers provide another resource to assist the organisation to provide a safe and respectful workplace</p>
  </div>

  <div class="abs overview"></div>
  <div class="abs overview-pill">OVERVIEW OF TRANING</div>
  <div class="abs overview-divider"></div>

  <div class="abs topic" style="left:26px;top:442px;width:196px">
    <h3><svg width="11" height="11" viewBox="0 0 12 12"><circle cx="6" cy="6" r="5" fill="none" stroke="#fff" stroke-width="1.3"/><path d="M3 5h6M6 5v4" stroke="#fff" stroke-width="1.3"/></svg>Discrimination</h3>
    <p>What is direct and indirect discrimination? What are the prescribed attributes? What are the exceptions to the general rules. Practical examples of behaviour that may be discriminatory.</p>
  </div>
  <div class="abs topic" style="left:26px;top:507px;width:196px">
    <h3><svg width="12" height="13" viewBox="0 0 12 13"><circle cx="4" cy="3" r="2" fill="none" stroke="#fff"/><path d="M2 12V7h4v5M7 8l4-3" stroke="#fff" fill="none"/></svg>Bullying</h3>
    <p style="margin-top:6px">What is bullying. Explore how bullying differs to discrimination or inappropriate behaviour. Performance Management - when it will and will not be bullying. Is all workplace conflict bullying? Practical examples of behaviour that may be bullying.</p>
  </div>
  <div class="abs topic" style="left:257px;top:444px;width:180px">
    <h3><svg width="14" height="12" viewBox="0 0 14 12"><circle cx="4" cy="2.5" r="1.8" fill="none" stroke="#fff"/><circle cx="10" cy="2.5" r="1.8" fill="none" stroke="#fff"/><path d="M1 11l3-6 3 6M7 11l3-6 3 6" stroke="#fff" fill="none"/></svg>Harassment</h3>
    <p style="margin-top:6px">What is harassment? Are protected attributes relevant to harassment? What is the difference between harassment and sexual harassment? How does the reasonable person test work in relation to harassment? Practical examples of behaviour that may be harassment or sexual harassment.</p>
  </div>
  <div class="abs topic" style="left:256px;top:535px;width:180px">
    <h3><svg width="12" height="12" viewBox="0 0 12 12"><circle cx="6" cy="3.5" r="2.3" fill="none" stroke="#fff"/><path d="M1 11h10M3 11l1-4h4l1 4" stroke="#fff" fill="none"/></svg>Victimisation and Vilification</h3>
    <p style="margin-top:7px">What is victimisation? What is Vilification?</p>
  </div>

  <div class="abs" style="left:26px;top:608px">
    <div class="footer-line"><svg width="9" height="9" viewBox="0 0 10 10"><circle cx="5" cy="5" r="4" fill="none" stroke="#333"/><path d="M1 5h8M5 1c-2 2-2 6 0 8M5 1c2 2 2 6 0 8" stroke="#333" fill="none" stroke-width=".8"/></svg>www.brooklegal.com.au</div>
    <div class="footer-line"><svg width="9" height="8" viewBox="0 0 10 8"><rect x=".5" y=".5" width="9" height="7" fill="none" stroke="#333"/><path d="M.5 .5l4.5 4 4.5-4" stroke="#333" fill="none"/></svg>info@brooklegal.au</div>
  </div>
  <div class="abs" style="left:386px;top:609px">
    <div class="social"><i></i>brooklegal.</div>
    <div class="social"><i></i>brooklegal.</div>
  </div>
  <div class="abs front-bar"></div>
</section>

<section class="page page--back">
  <div class="abs back-dark"></div>
  <div class="abs back-divider"></div>

  <div class="abs topic" style="left:34px;top:55px;width:188px">
    <h3><svg width="11" height="11" viewBox="0 0 12 12"><path d="M6 1v7M3 5l3 3 3-3M1 11h10" stroke="#fff" fill="none" stroke-width="1.4"/></svg>Adverse Action</h3>
    <p style="font-size:6.9px">What is adverse action and how does it differ to other unlawful behaviour? What is a workplace right? When is it lawful to terminate employment because of an employee's absence? How are the protected attributes relevant to adverse action?</p>
  </div>
  <div class="abs topic" style="left:31px;top:127px;width:195px">
    <h3><svg width="13" height="13" viewBox="0 0 14 14"><circle cx="7" cy="4.5" r="3" fill="none" stroke="#fff"/><path d="M1.5 13c0-3 2.5-5 5.5-5s5.5 2 5.5 5z" fill="none" stroke="#fff"/></svg>The Contact Officer's role</h3>
    <p style="margin-top:10px;font-size:7px">How to perform your role when approached by an employee – the 6 step approach. What not to do. What are the obligations with regard to Confidentiality?</p>
  </div>
  <div class="abs topic" style="left:254px;top:52px;width:190px">
    <h3><svg width="13" height="13" viewBox="0 0 14 14"><circle cx="7" cy="7" r="6" fill="none" stroke="#fff"/><circle cx="4.5" cy="7" r=".8" fill="#fff"/><circle cx="7" cy="7" r=".8" fill="#fff"/><circle cx="9.5" cy="7" r=".8" fill="#fff"/></svg>Grievance Options</h3>
    <p style="font-size:6.9px">Explore the options of complaint management - self management, internal informal management, formal internal management. How do they compare and what are the advantages and disadvantages of each approach. Is doing nothing an option? External options – advantages and disadvantages. Who decides which option?</p>
  </div>
  <div class="abs topic" style="left:257px;top:151px;width:180px">
    <h3><svg width="12" height="14" viewBox="0 0 12 14"><path d="M1 1h7l3 3v9H1z" fill="none" stroke="#fff"/><path d="M3 6h6M3 8h6M3 10h6" stroke="#fff" stroke-width=".8"/></svg>Test Learning</h3>
    <p style="margin-top:7px">Role play, group discussion</p>
  </div>

  <div class="abs outcomes-bar">LEARNING OUTCOMES</div>
  <p class="abs outcomes-intro">Training will enable participants to perform their role of Contact Officer and to understand</p>
  <ul class="abs outcomes">
    <li><svg width="12" height="12" viewBox="0 0 12 12"><circle cx="6" cy="6" r="5.2" fill="none" stroke="#1f8ae6" stroke-width="1.2"/><path d="M3 6l2.3 2.3L11 1.5" fill="none" stroke="#1f8ae6" stroke-width="1.4"/></svg>The role and responsibilities of a Contact Officer</li>
    <li><svg width="12" height="12" viewBox="0 0 12 12"><circle cx="6" cy="6" r="5.2" fill="none" stroke="#1f8ae6" stroke-width="1.2"/><path d="M3 6l2.3 2.3L11 1.5" fill="none" stroke="#1f8ae6" stroke-width="1.4"/></svg>What amounts to unlawful workplace behaviour</li>
    <li><svg width="12" height="12" viewBox="0 0 12 12"><circle cx="6" cy="6" r="5.2" fill="none" stroke="#1f8ae6" stroke-width="1.2"/><path d="M3 6l2.3 2.3L11 1.5" fill="none" stroke="#1f8ae6" stroke-width="1.4"/></svg>What is considered inappropriate behaviour in our workplace</li>
    <li><svg width="12" height="12" viewBox="0 0 12 12"><circle cx="6" cy="6" r="5.2" fill="none" stroke="#1f8ae6" stroke-width="1.2"/><path d="M3 6l2.3 2.3L11 1.5" fill="none" stroke="#1f8ae6" stroke-width="1.4"/></svg>How to apply understanding unlawful/inappropriate behaviour to<br>common scenarios</li>
    <li><svg width="12" height="12" viewBox="0 0 12 12"><circle cx="6" cy="6" r="5.2" fill="none" stroke="#1f8ae6" stroke-width="1.2"/><path d="M3 6l2.3 2.3L11 1.5" fill="none" stroke="#1f8ae6" stroke-width="1.4"/></svg>How to address and resolve grievances early</li>
    <li><svg width="12" height="12" viewBox="0 0 12 12"><circle cx="6" cy="6" r="5.2" fill="none" stroke="#1f8ae6" stroke-width="1.2"/><path d="M3 6l2.3 2.3L11 1.5" fill="none" stroke="#1f8ae6" stroke-width="1.4"/></svg>Options to resolve grievances internally and the Contact Officer role</li>
    <li><svg width="12" height="12" viewBox="0 0 12 12"><circle cx="6" cy="6" r="5.2" fill="none" stroke="#1f8ae6" stroke-width="1.2"/><path d="M3 6l2.3 2.3L11 1.5" fill="none" stroke="#1f8ae6" stroke-width="1.4"/></svg>External options and their pros and cons for resolving grievances</li>
  </ul>

  <div class="abs contact-band">
    <div class="abs contact-list">
      <div><svg width="7" height="9" viewBox="0 0 8 10"><path d="M4 9.5S.8 5.8.8 3.6a3.2 3.2 0 016.4 0C7.2 5.8 4 9.5 4 9.5z" fill="none" stroke="#fff"/><circle cx="4" cy="3.6" r="1.1" fill="#fff"/></svg>48 Harbour Lane Hobart 7000</div>
      <div><svg width="7" height="8" viewBox="0 0 8 8"><path d="M1 1.2l1.6-.4 1 1.8-1 .8a5 5 0 002 2l.8-1 1.8 1-.4 1.6C3.6 7.6.4 4.4 1 1.2z" fill="#fff"/></svg>(03) 6210 4471</div>
      <div><svg width="7" height="9" viewBox="0 0 8 10"><path d="M4 9.5S.8 5.8.8 3.6a3.2 3.2 0 016.4 0C7.2 5.8 4 9.5 4 9.5z" fill="none" stroke="#fff"/><circle cx="4" cy="3.6" r="1.1" fill="#fff"/></svg>12 Quay Road Melbourne 3000</div>
      <div><svg width="7" height="8" viewBox="0 0 8 8"><path d="M1 1.2l1.6-.4 1 1.8-1 .8a5 5 0 002 2l.8-1 1.8 1-.4 1.6C3.6 7.6.4 4.4 1 1.2z" fill="#fff"/></svg>(03) 9480 2236</div>
    </div>
    <div class="abs brand back-brand"><span class="brand__dot"></span>Brook Legal</div>
  </div>

  <div class="abs" style="left:34px;top:597px">
    <div class="footer-line" style="font-size:9px"><svg width="10" height="10" viewBox="0 0 10 10"><circle cx="5" cy="5" r="4" fill="none" stroke="#333"/><path d="M1 5h8M5 1c-2 2-2 6 0 8M5 1c2 2 2 6 0 8" stroke="#333" fill="none" stroke-width=".8"/></svg>www.brooklegal.com.au</div>
    <div class="footer-line" style="font-size:9px"><svg width="10" height="8" viewBox="0 0 10 8"><rect x=".5" y=".5" width="9" height="7" fill="none" stroke="#333"/><path d="M.5 .5l4.5 4 4.5-4" stroke="#333" fill="none"/></svg>info@brooklegal.au</div>
  </div>
  <div class="abs" style="left:360px;top:597px">
    <div class="social" style="font-size:8.5px;gap:9px"><i style="width:6px;height:6px"></i>brooklegal.</div>
    <div class="social" style="font-size:8.5px;gap:9px"><i style="width:6px;height:6px"></i>brooklegal.</div>
  </div>
  <div class="abs back-bottom"></div>
</section>

</body>
</html>
```